Brisk Nook needs a packaging design

Hello!

I need an eye-catching package design for Brisk Nook mobile accessories. The products inside the box package include a bluetooth speaker and a power bank.

This is under our brandname called Brisk Nook. The text should be in the picture, no matter how the design looks.

I have attached pictures of the products. If you think that there will not be well with the images it is ok. Then these texts be included:
Bluetooth Speaker
Power Bank

This is our slogan:
Music + Power. It's your imagination that sets the limits!

The image will be printed on a carton pack containing with four color printing. Customising the picture for the type of print.

Should be in 300 DPI High resolution.

Please check the attached pictures where your design will be printed.
Also, I attached design inspiration images for reference. Feel free to do something similar like that.

For the size and dimensions please refer to this attachment:

So remember, the important thing is the design. Do your absolute best!
Updates

Reason: Hello everyone! I would like to see a design without the images of the accessories. Only text. I also dont want the text "Its you imagination that sets...". Thank you!

Target Market(s)

Mobile accessories

Industry/Entity Type

Electronics

Requirements
Must have
• This text:
• Brisk Nook
Nice to have
• Music + Power.

```html
<!DOCTYPE html>
<html lang="en">
<head>
<meta charset="utf-8">
<title>Brisk Nook – Packaging Layout</title>
<link rel="stylesheet" href="https://fonts.googleapis.com/css2?family=Arimo&family=Krona+One&family=Michroma&display=swap">
<style>
  :root {
    --paper: #ffffff;
    --ink: #111111;
    --box-dark: #050806;
    --box-mid: #1c1f1d;
    --glow-green: #1fae3c;
    --glow-lime: #d6f25e;
    --text-white: #f4f6f2;
    --text-yellow: #f2e21a;
    --fold-line: rgba(255,255,255,0.35);
  }
  * { margin: 0; padding: 0; box-sizing: border-box; }
  html, body { width: 1200px; height: 1200px; overflow: hidden; background: var(--paper); }
  .layout { position: relative; width: 1200px; height: 1200px; }

  .panel-label {
    position: absolute;
    font-family: "Arimo", Arial, sans-serif;
    font-size: 26px;
    color: var(--ink);
    white-space: nowrap;
  }
  .panel-label--top { left: 679px; top: 112px; transform: translateX(-50%); }
  .panel-label--bottom { left: 679px; top: 1047px; transform: translateX(-50%); }
  .panel-label--left { left: 123px; top: 503px; transform: translate(-50%, -50%) rotate(-90deg); }

  .artwork { position: absolute; left: 0; top: 0; }

  .product-line {
    font-family: "Michroma", sans-serif;
    font-variant: small-caps;
    font-size: 22px;
    fill: var(--text-white);
  }
  .brand-name {
    font-family: "Krona One", sans-serif;
    font-size: 50px;
    fill: var(--text-white);
  }
  .tagline {
    font-family: "Michroma", sans-serif;
    font-variant: small-caps;
    font-size: 31px;
    fill: var(--text-yellow);
    stroke: #3a3300;
    stroke-width: 0.6;
  }
  .range-line {
    font-family: "Michroma", sans-serif;
    font-size: 27px;
    fill: var(--text-white);
  }
</style>
</head>
<body>
<main class="layout">
  <span class="panel-label panel-label--top">TOP PANEL</span>
  <span class="panel-label panel-label--left">SIDE PANEL</span>
  <span class="panel-label panel-label--bottom">SIDE PANEL</span>

  <svg class="artwork" width="1200" height="1200" viewBox="0 0 1200 1200">
    <defs>
      <clipPath id="box-shape">
        <path d="M152 152 H1035 V1035 H318 V869 H152 Z"/>
      </clipPath>
      <linearGradient id="box-bg" x1="0" y1="0" x2="0" y2="1">
        <stop offset="0" stop-color="var(--box-mid)"/>
        <stop offset="0.5" stop-color="var(--box-dark)"/>
        <stop offset="1" stop-color="var(--box-mid)"/>
      </linearGradient>
      <linearGradient id="light-swoosh" x1="0" y1="0" x2="1" y2="0">
        <stop offset="0" stop-color="var(--glow-lime)" stop-opacity="0.95"/>
        <stop offset="0.45" stop-color="var(--glow-green)" stop-opacity="0.85"/>
        <stop offset="1" stop-color="var(--glow-green)" stop-opacity="0.3"/>
      </linearGradient>
      <filter id="soft-blur" x="-20%" y="-50%" width="140%" height="200%">
        <feGaussianBlur stdDeviation="22"/>
      </filter>
    </defs>

    <g clip-path="url(#box-shape)">
      <rect x="152" y="152" width="883" height="883" fill="url(#box-bg)"
            role="img" aria-label="Dark honeycomb mesh texture background"/>
      <path d="M152 400 C380 360 560 560 760 520 C880 495 960 520 1035 540 L1035 640 C940 610 860 610 760 630 C560 670 380 560 152 620 Z"
            fill="url(#light-swoosh)" filter="url(#soft-blur)"
            role="img" aria-label="Glowing green and lime light streak"/>
      <line x1="318" y1="152" x2="318" y2="1035" stroke="var(--fold-line)" stroke-width="1.5"/>
      <line x1="318" y1="869" x2="1035" y2="869" stroke="var(--fold-line)" stroke-width="1.5"/>
    </g>

    <text class="product-line" x="363" y="208" textLength="625" lengthAdjust="spacingAndGlyphs">Bluetooth Speaker + Power Bank</text>
    <text class="brand-name" x="403" y="546" textLength="548" lengthAdjust="spacingAndGlyphs">BRISK NOOK</text>
    <text class="tagline" x="486" y="596" textLength="391" lengthAdjust="spacingAndGlyphs">Music + Power</text>
    <text class="range-line" x="985" y="780" text-anchor="end" textLength="262" lengthAdjust="spacingAndGlyphs">ALL MOBILE</text>
    <text class="range-line" x="985" y="821" text-anchor="end" textLength="313" lengthAdjust="spacingAndGlyphs">ACCESSORIES</text>
  </svg>
</main>
</body>
</html>
```